New Web Design Project

New Roofing Website homepage mockup

Complete design document here: https://files.plenovark.com/document/d/7kRtWmZpQ2vLxB9nHcYdF4sJgTuEaOiMbNwXzCyVqhr/edit?usp=sharing
Updates

PROJECT IS NOW CLOSED. ANY NEW SUBMISSIONS WILL BE AUTO REJECTED

Number of Pages Required

1 page

Font styles to use
Sans Serif

```html
<!DOCTYPE html>
<html lang="en">
<head>
<meta charset="utf-8">
<title>Summitcrest Roofing — Homepage</title>
<link href="https://fonts.googleapis.com/css2?family=Montserrat:wght@400;500;600;700;800&display=swap" rel="stylesheet">
<style>
:root{
  --blue:#2c9ee0;
  --blue-bright:#3bb1ee;
  --blue-deep:#2a6fa8;
  --ink:#111;
  --grey-bg:#ececec;
  --text:#555;
  --white:#fff;
}
*{box-sizing:border-box;margin:0;padding:0}
html,body{width:1200px;height:3706px;overflow:hidden}
body{font-family:"Montserrat",sans-serif;color:var(--ink);background:var(--white);position:relative}
.abs{position:absolute}
.topbar{left:0;top:0;width:1200px;height:26px;background:var(--blue);color:#fff;font-size:12px}
.topbar .mail{left:160px;top:6px}
.topbar .phone{left:850px;top:6px}
.topbar .dots{left:962px;top:8px;display:flex;gap:9px}
.topbar .dots span{width:9px;height:9px;border-radius:50%;background:#fff;opacity:.9}
.nav{left:0;top:26px;width:1200px;height:71px;background:#fff}
.brand{display:flex;align-items:center;gap:6px;font-weight:700;color:var(--blue);font-size:15px}
.brand i{width:12px;height:12px;background:var(--blue);display:block;flex:none}
.nav .brand{left:162px;top:19px;font-size:12px;line-height:15px;width:130px}
.nav ul{list-style:none;left:0;top:0;width:1200px;height:71px;font-size:12px}
.nav li{position:absolute;top:32px;white-space:nowrap}
.nav .cta{left:868px;top:21px;width:172px;height:36px;border:1px solid var(--blue);color:var(--blue);font-size:12px;display:flex;align-items:center;justify-content:center;border-radius:2px}
.hero{left:0;top:97px;width:1200px;height:424px;background:linear-gradient(100deg,#2c3644 0%,#3d4652 45%,#6a5246 70%,#b0642e 85%,#4a3a30 100%)}
.hero h1{left:158px;top:82px;font-size:46px;font-weight:800;line-height:56px;color:#fff}
.hero h1 span{color:var(--blue-bright);display:block}
.hero p{left:165px;top:200px;width:360px;font-size:11px;color:#fff;line-height:14px}
.btn{background:var(--blue);color:#fff;font-weight:700;font-size:12px;display:flex;align-items:center;justify-content:center;border-radius:2px}
.hero .btn{left:158px;top:245px;width:104px;height:30px}
.services{left:0;top:521px;width:1200px;height:725px;background:var(--grey-bg)}
.section-title{width:1200px;left:0;text-align:center;font-weight:800;font-size:30px}
.rule{width:86px;height:3px;background:var(--blue);left:557px}
.tile{display:flex;align-items:center;justify-content:center;text-align:center;color:#fff;font-size:18px}
.tile.big{font-weight:800;font-size:19px;line-height:22px}
.about{left:0;top:1246px;width:1200px;height:305px;overflow:hidden}
.about .photo{left:0;top:0;width:1200px;height:305px;background:linear-gradient(160deg,#c9d8e2 0%,#d7c08a 55%,#9a7a3c 100%)}
.about h2{left:162px;top:56px;font-size:26px;font-weight:800;color:#fff}
.about .line{left:160px;top:90px;width:300px;height:1px;background:#fff;opacity:.7}
.about p{left:160px;top:108px;width:380px;font-size:14px;line-height:22px;color:#fff;font-weight:500}
.about .more{left:160px;top:212px;width:118px;height:36px;background:#fff;color:var(--blue);font-size:14px;display:flex;align-items:center;justify-content:center;border-radius:2px}
.projects{left:0;top:1551px;width:1200px;height:787px;background:#eeeeee}
.grid{left:164px;top:180px;width:872px;height:530px;display:grid;grid-template-columns:repeat(3,1fr);grid-template-rows:repeat(2,1fr)}
.label-box{left:39px;top:36px;width:207px;height:200px;background:rgba(59,177,238,.8);color:#fff;font-size:27px;font-weight:800;display:flex;align-items:center;justify-content:center}
.cost{left:0;top:2338px;width:1200px;height:314px;background:var(--blue-deep);color:#fff;text-align:center}
.cost h2{left:0;width:1200px;top:70px;font-size:30px;font-weight:500}
.cost p{left:300px;width:600px;top:132px;font-size:16px;line-height:20px}
.cost .btn{left:410px;top:193px;width:380px;height:45px;background:var(--blue-bright);font-size:18px;font-weight:500}
.clients{left:0;top:2652px;width:1200px;height:650px;background:linear-gradient(180deg,#f4f1ee,#ebe6e1)}
.card{left:259px;top:214px;width:682px;height:359px;background:#fff;border:1px solid #ccc}
.avatar{left:531px;top:165px;width:116px;height:116px;border-radius:50%;background:linear-gradient(#d8d2cc,#b9aea4);border:4px solid #fff}
.card .q{font-size:90px;color:#ccc;font-weight:800;line-height:1}
.card p{left:50px;top:118px;width:582px;text-align:center;font-size:12px;line-height:22.5px;color:var(--text)}
.card .who{left:0;width:682px;top:295px;text-align:center;font-size:18px;line-height:23px;color:#222}
.footer{left:0;top:3302px;width:1200px;height:404px;background:linear-gradient(180deg,#2c9ee0,#2484c9)}
.footer h3{font-size:17px;font-weight:700;color:#fff}
.footer ul{list-style:none;font-size:12px;color:#fff}
.footer li{height:30px}
.footer li::before{content:"» "}
.contact li::before{content:none}
.contact li{display:flex;gap:10px;align-items:flex-start}
.contact svg{flex:none;margin-top:2px}
.news p{font-size:11px;color:#fff;line-height:18px;width:260px}
.input{left:767px;top:157px;width:279px;height:36px;background:#fff;border-radius:18px;font-size:11px;color:#333;padding:11px 0 0 22px}
.socials{left:787px;top:215px;display:flex;gap:19px}
.socials span{width:26px;height:26px;border-radius:50%;background:#2270b7;border:1px solid rgba(255,255,255,.5)}
.footer .brand{left:0;width:1200px;justify-content:center;top:300px;color:#fff;font-size:20px}
.footer .brand i{background:#fff;width:16px;height:16px}
</style>
</head>
<body>

<header class="abs topbar">
  <span class="abs mail">✉ hello@summitcrestroofing.com</span>
  <span class="abs phone">☎ 555-210-4478</span>
  <span class="abs dots"><span></span><span></span><span></span><span></span></span>
</header>

<nav class="abs nav">
  <div class="abs brand"><i></i><span>SUMMITCREST<br>ROOFING</span></div>
  <ul class="abs">
    <li style="left:315px">Home</li>
    <li style="left:380px">About</li>
    <li style="left:445px">Services</li>
    <li style="left:517px">Affiliations</li>
    <li style="left:599px">Reviews</li>
    <li style="left:669px">Project</li>
    <li style="left:735px">Member</li>
    <li style="left:812px">Blog</li>
  </ul>
  <div class="abs cta">Get An Instant Estimate</div>
</nav>

<section class="abs hero" role="img" aria-label="Roofer nailing shingles on a roof">
  <h1 class="abs">BUILT RIGHT<span>BUILT TO LAST</span></h1>
  <p class="abs">Lorem ipsum dolor sit amet, consectetur adipiscing elit,sed do eiusmod tempor incididunt ut labore et</p>
  <div class="abs btn">Read more</div>
</section>

<section class="abs services">
  <h2 class="abs section-title" style="top:68px">SERVICES</h2>
  <div class="abs rule" style="top:112px"></div>
  <div class="abs tile big" style="left:160px;top:167px;width:265px;height:309px;background:linear-gradient(#3d5a78,#6a4a52)" role="img" aria-label="New roof installation on a house">ROOF<br>INSTALLATION</div>
  <div class="abs" style="left:436px;top:181px;width:324px;height:304px;background:linear-gradient(135deg,#fff 20%,#e8d2a6 50%,#f5f5f5 80%)" role="img" aria-label="Cutaway drawing of a roof structure"></div>
  <div class="abs tile big" style="left:774px;top:167px;width:265px;height:309px;background:linear-gradient(#3e5670,#5b4a46)" role="img" aria-label="Roofer repairing tiles">ROOF<br>REPAIR</div>
  <div class="abs tile" style="left:160px;top:494px;width:204px;height:162px;background:linear-gradient(#55443a,#8b6a50)" role="img" aria-label="Attic with skylight windows">Windows<br>Skylights/</div>
  <div class="abs tile" style="left:384px;top:494px;width:205px;height:162px;background:linear-gradient(#6c6258,#8a7866)" role="img" aria-label="Gutters on a house">Gutters</div>
  <div class="abs tile" style="left:609px;top:494px;width:205px;height:162px;background:linear-gradient(#41566a,#6d7478)" role="img" aria-label="House siding">Siding</div>
  <div class="abs tile" style="left:835px;top:494px;width:204px;height:162px;background:linear-gradient(#7a6050,#9a7a62)" role="img" aria-label="Interior with leak damage">leak damage<br>repairs</div>
</section>

<section class="abs about">
  <div class="abs photo" role="img" aria-label="House with metal roof and yellow siding"></div>
  <svg class="abs" style="left:0;top:0" width="1200" height="305"><polygon points="0,0 658,0 460,305 0,305" fill="#3bb1ee"/></svg>
  <h2 class="abs">ABOUT US</h2>
  <div class="abs line"></div>
  <p class="abs">After over a decade of general contracting, we continue to see a repetitive trend by the roof purchase process where homeowners are constantly ,left confused</p>
  <div class="abs more">Read More</div>
</section>

<section class="abs projects">
  <h2 class="abs section-title" style="top:70px;font-size:28px">RECENT PROJECTS</h2>
  <div class="abs rule" style="top:116px"></div>
  <div class="abs grid">
    <div style="position:relative;background:linear-gradient(#8fa8c0,#6f7d88)" role="img" aria-label="Shingle-style house in Lexington"><div class="abs label-box">Lexington</div></div>
    <div style="background:linear-gradient(#9fb8d4,#6f8a5a)" role="img" aria-label="Large grey colonial home with lawn"></div>
    <div style="background:linear-gradient(#8aa6c6,#4d4f52)" role="img" aria-label="Roof cupola with weathervane"></div>
    <div style="background:linear-gradient(#5a5552,#c4b3a0)" role="img" aria-label="Curved roof over arched windows"></div>
    <div style="background:linear-gradient(#54663e,#8d9aa0)" role="img" aria-label="Aerial view of a white house"></div>
    <div style="background:linear-gradient(#4e6a3c,#4c5458)" role="img" aria-label="Grey house among trees"></div>
  </div>
</section>

<section class="abs cost">
  <h2 class="abs">HOW MUCH DOES A NEW ROOF COST?</h2>
  <p class="abs">A roof does more than keep the rain off your head. It protects your biggest investment – your home.</p>
  <div class="abs btn">Calculate the cost of a new Roof now</div>
</section>

<section class="abs clients" role="img" aria-label="Faded collage of client portraits">
  <h2 class="abs section-title" style="top:68px;font-size:28px">HAPPY CLIENTS</h2>
  <div class="abs rule" style="top:112px"></div>
  <svg class="abs" style="left:168px;top:370px" width="22" height="36"><polyline points="18,2 4,18 18,34" fill="none" stroke="#2c9ee0" stroke-width="4"/></svg>
  <svg class="abs" style="left:1010px;top:370px" width="22" height="36"><polyline points="4,2 18,18 4,34" fill="none" stroke="#2c9ee0" stroke-width="4"/></svg>
  <div class="abs card">
    <span class="abs q" style="left:14px;top:10px">“</span>
    <span class="abs q" style="right:20px;top:230px">”</span>
    <p class="abs">"We needed to put a new roof on our house, as well as repair a sagging porch roof. Shingles had been flying off and we had had several leaks. Owen provided a very reasonable estimate - well below some of the other HomeHelp Directory companies. The work was done very promptly and professionally. A couple of issues that arose were settled to our satisfaction and Owen took full ownership of the situation. It was very clear that customer satisfaction is a priority for this company. I would definitely recommend and hire again."</p>
    <div class="abs who">Dan<br>Waltham</div>
  </div>
  <div class="abs avatar" role="img" aria-label="Client portrait"></div>
</section>

<footer class="abs footer">
  <h3 class="abs" style="left:166px;top:62px">Information</h3>
  <ul class="abs" style="left:166px;top:117px"><li>About Us</li><li>Help Desk</li><li>Support</li><li>Privacy Policy</li><li>Terms &amp; Condition</li></ul>
  <h3 class="abs" style="left:354px;top:62px">Userful Link</h3>
  <ul class="abs" style="left:354px;top:117px"><li>Homepage</li><li>Submit Job</li><li>All Candidates</li><li>Latest Blogs</li><li>JObs</li></ul>
  <h3 class="abs" style="left:522px;top:62px">Contact Us</h3>
  <ul class="abs contact" style="left:522px;top:117px;width:200px">
    <li style="height:46px"><svg width="10" height="13"><path d="M5 0a5 5 0 0 1 5 5c0 4-5 8-5 8S0 9 0 5a5 5 0 0 1 5-5z" fill="#fff"/><circle cx="5" cy="5" r="2" fill="#2c9ee0"/></svg><span>Lorem ipsum dolor sit amet, consectetur</span></li>
    <li style="height:36px"><svg width="11" height="11"><path d="M2 0l3 3-1.5 2a7 7 0 0 0 2.5 2.5L8 6l3 3-2 2C4 11 0 7 0 2z" fill="#fff"/></svg><span>+1800-555-0192</span></li>
    <li style="height:36px"><svg width="12" height="9"><rect width="12" height="9" fill="#fff"/><polyline points="0,0 6,5 12,0" fill="none" stroke="#2c9ee0"/></svg><span>care@summitcrestroofing.com</span></li>
    <li><svg width="11" height="11"><circle cx="5.5" cy="5.5" r="5.5" fill="#fff"/></svg><span>summitcrest.help</span></li>
  </ul>
  <h3 class="abs" style="left:764px;top:62px">Subscribe our Newsletter</h3>
  <div class="abs news" style="left:764px;top:112px"><p>Lorem ipsum dolor sit amet, consectetur and ipdate</p></div>
  <div class="abs input">Enter Your Email Id</div>
  <svg class="abs" style="left:1006px;top:165px" width="22" height="20"><polygon points="0,9 22,0 16,20 10,12" fill="#2c9ee0"/></svg>
  <div class="abs socials"><span></span><span></span><span></span><span></span><span></span></div>
  <div class="abs brand"><i></i>SUMMITCREST ROOFING</div>
</footer>

</body>
</html>
```